Breast Cancer Car Donation Website Design

Please create a new one page website design.

Current site: http://www.givemyautohope.com/

The NEW website address will be RidesforPinkRibbonAid.org

Use these sites for an idea of what I am looking for. I like these sites best: drivesforheroesfund.org and autosforservicemen.org

```html
<!DOCTYPE html>
<html lang="en">
<head>
<meta charset="utf-8">
<title>RidesforPinkRibbonAid.org – Donate Your Car &amp; Boat</title>
<link href="https://fonts.googleapis.com/css2?family=Marcellus&family=Lobster&family=Lato:wght@400;700&display=swap" rel="stylesheet">
<style>
:root{
  --pink:#e6197a;
  --pink-dark:#c70f66;
  --pink-soft:#f7d3e5;
  --ink:#333333;
  --muted:#6b6b6b;
  --grey:#f1f1f1;
  --grey-line:#dddddd;
  --white:#ffffff;
}
*{box-sizing:border-box;margin:0;padding:0}
html,body{width:1200px;height:4128px;overflow:hidden;background:var(--white)}
body{font-family:'Lato',Arial,sans-serif;color:var(--ink);position:relative}
section,header,footer{position:absolute;left:0;width:1200px}
.btn{display:inline-block;background:var(--pink);color:var(--white);font-family:'Marcellus',Georgia,serif;font-size:22px;letter-spacing:1px;padding:14px 30px;border-radius:4px}
.btn-outline{border:2px solid var(--white);background:transparent}

/* header */
.site-header{top:0;height:132px;border-bottom:4px solid var(--pink)}
.brand{position:absolute;left:78px;top:12px;display:flex;align-items:center;gap:12px}
.brand-dot{width:26px;height:26px;border-radius:50%;background:var(--pink)}
.brand-name{font-family:'Lato',sans-serif;font-weight:700;font-size:22px;color:var(--pink)}
.phone-top{position:absolute;right:80px;top:14px;font-family:'Marcellus',serif;font-size:36px;color:var(--pink);display:flex;align-items:center;gap:12px}
.nav{position:absolute;right:78px;top:78px;display:flex;gap:6px}
.nav span{height:54px;line-height:54px;padding:0 26px;background:var(--grey);font-size:15px;font-weight:700;color:#444;border-radius:6px 6px 0 0}
.nav .active{background:var(--pink);color:var(--white)}
.nav .search{padding:0 20px}

/* hero */
.hero{top:132px;height:543px;background:linear-gradient(120deg,#8fa56f 0%,#c9b89a 40%,#e8c9c9 70%,#b9a48c 100%);text-align:center}
.hero-title{position:absolute;top:150px;left:0;width:100%;font-family:'Lobster',cursive;font-weight:400;font-size:62px;line-height:78px;color:var(--white);text-shadow:0 3px 6px rgba(0,0,0,.45)}
.hero-sub{position:absolute;top:318px;left:0;width:100%;font-family:'Marcellus',serif;font-size:21px;color:var(--white);text-shadow:0 2px 4px rgba(0,0,0,.5)}
.hero .btn{position:absolute;top:362px;left:50%;transform:translateX(-50%)}

/* donate form */
.donate-band{top:675px;height:261px;background:var(--pink);color:var(--white)}
.ribbon-tab{position:absolute;left:78px;top:-42px;width:100px;height:110px;background:var(--pink);border-radius:50px 50px 0 0}
.donate-title{position:absolute;left:180px;top:38px;font-family:'Marcellus',serif;font-weight:400;font-size:30px}
.donate-note{position:absolute;left:182px;top:80px;font-size:15px}
.form-grid{position:absolute;left:182px;top:115px;width:940px;display:grid;grid-template-columns:repeat(4,1fr);gap:14px 12px}
.field{height:44px;background:var(--white);color:#777;font-size:13px;padding:0 14px;line-height:44px;border-radius:3px;position:relative}
.field.select::after{content:"";position:absolute;right:14px;top:19px;border:6px solid transparent;border-top-color:#444}
.field.submit{background:transparent;border:2px solid var(--white);color:var(--white);text-align:center;font-family:'Marcellus',serif;font-size:17px;line-height:40px}

/* steps */
.steps{top:936px;height:460px;text-align:center}
.section-title{font-family:'Marcellus',serif;font-weight:400;font-size:34px;line-height:44px;color:var(--pink);text-align:center}
.steps .section-title{position:absolute;top:60px;width:100%}
.step-list{position:absolute;top:180px;left:180px;width:840px;display:flex;justify-content:space-between}
.step{width:260px;text-align:center}
.step-circle{width:130px;height:130px;border-radius:50%;background:var(--grey);margin:0 auto 26px;display:flex;align-items:center;justify-content:center}
.step p{font-family:'Marcellus',serif;font-size:18px;line-height:26px}

/* why */
.why{top:1396px;height:415px;background:var(--grey)}
.why-photo{position:absolute;left:0;top:0;width:600px;height:415px;background:linear-gradient(135deg,#d9d9d9,#f4f4f4 55%,#cfc6c0)}
.round-arrow{position:absolute;width:46px;height:46px;border-radius:50%;background:var(--pink);display:flex;align-items:center;justify-content:center}
.why .round-arrow{left:577px;top:188px}
.why-copy{position:absolute;left:656px;top:42px;width:470px}
.why-copy h2{font-family:'Marcellus',serif;font-size:36px;line-height:44px;color:var(--pink);font-weight:400}
.why-copy p{margin-top:22px;font-size:14px;line-height:24px;color:var(--muted)}
.why-copy .btn{margin-top:22px;font-size:19px;padding:12px 30px}

/* veterans */
.veterans{top:1811px;height:418px}
.veterans .section-title{position:absolute;top:60px;width:100%}
.perk-list{position:absolute;top:175px;left:70px;width:1060px;display:flex;justify-content:space-between}
.perk{width:170px;text-align:center}
.perk-circle{width:104px;height:104px;border-radius:50%;background:var(--pink);margin:0 auto 24px;display:flex;align-items:center;justify-content:center}
.perk p{font-family:'Marcellus',serif;font-size:16px;line-height:22px}

/* screening */
.screening{top:2229px;height:207px;background:var(--pink);color:var(--white)}
.screen-photo{position:absolute;left:85px;top:20px;width:320px;height:187px;background:linear-gradient(180deg,#f29cc3,#d75594);border-radius:4px 4px 0 0}
.screening h3{position:absolute;left:428px;top:40px;font-family:'Marcellus',serif;font-size:30px;line-height:40px;font-weight:400}
.checks{position:absolute;left:432px;top:140px;display:flex;gap:34px;font-size:14px}
.checks span{display:flex;align-items:center;gap:10px}
.screening .btn{position:absolute;right:80px;top:80px;font-size:19px;padding:12px 20px}

/* about */
.about{top:2436px;height:418px;background:var(--grey)}
.about-copy{position:absolute;left:80px;top:58px;width:440px}
.about-copy h2{font-family:'Marcellus',serif;font-size:32px;color:var(--pink);font-weight:400}
.about-copy h4{margin-top:8px;font-size:15px;font-weight:700}
.about-copy p{margin-top:10px;font-size:14px;line-height:24px;color:var(--muted)}
.about-copy .btn{margin-top:20px;font-size:19px;padding:12px 30px}
.about-copy .org-link{display:block;margin-top:20px;font-size:15px;font-style:italic;font-weight:700;text-decoration:underline}
.about-photo{position:absolute;left:600px;top:0;width:600px;height:418px;background:linear-gradient(160deg,#8fb07a,#c7cfa4 45%,#e7a8c6 80%,#d9709f)}
.about .round-arrow{left:577px;top:186px}

/* faq */
.faq{top:2854px;height:696px}
.faq .section-title{position:absolute;top:52px;width:100%}
.faq-list{position:absolute;top:112px;left:254px;width:692px}
.faq-item{background:var(--grey);margin-bottom:6px;height:51px;padding:0 22px;display:flex;align-items:center;justify-content:space-between;font-size:14px}
.faq-item.open{background:#e6e6e6}
.faq-answer{padding:18px 22px 22px;font-size:14px;line-height:24px;color:var(--muted);margin-bottom:6px}
.faq-answer a{color:var(--pink);text-decoration:underline;font-weight:700}
.toggle{width:22px;height:22px;border-radius:50%;background:var(--pink);color:var(--white);display:flex;align-items:center;justify-content:center;font-size:18px;line-height:1;font-weight:700}

/* pickup */
.pickup{top:3550px;height:372px}
.pickup-band{position:absolute;left:0;top:124px;width:1200px;height:248px;background:var(--pink)}
.car-photo{position:absolute;left:278px;top:0;width:642px;height:212px;background:linear-gradient(180deg,#f5d6e6,#e9a8c8 70%,#b9b9b9);border-radius:180px 220px 40px 40px}
.pickup-label{position:absolute;top:226px;width:100%;text-align:center;color:var(--white);font-family:'Marcellus',serif;font-size:32px}
.pickup-phone{position:absolute;top:266px;width:100%;text-align:center;color:var(--white);font-family:'Marcellus',serif;font-size:64px}

/* footer */
.site-footer{top:3922px;height:206px}
.foot-org{position:absolute;left:128px;top:46px;display:flex;align-items:center;gap:12px}
.foot-square{width:34px;height:34px;background:var(--pink)}
.foot-name{font-weight:700;font-size:16px;color:var(--pink);width:150px;line-height:20px}
.foot-text{position:absolute;left:364px;top:42px;width:680px;font-size:13px;line-height:22px;color:var(--muted)}
.foot-copy{position:absolute;left:364px;top:128px;font-size:13px;font-weight:700}
</style>
</head>
<body>

<header class="site-header">
  <div class="brand"><span class="brand-dot"></span><span class="brand-name">RidesforPinkRibbonAid.org</span></div>
  <div class="phone-top">
    <svg width="30" height="30" viewBox="0 0 24 24"><path fill="#e6197a" d="M6.6 10.8a15 15 0 0 0 6.6 6.6l2.2-2.2c.3-.3.7-.4 1-.2 1.1.4 2.3.6 3.6.6.6 0 1 .4 1 1V20c0 .6-.4 1-1 1A17 17 0 0 1 3 4c0-.6.4-1 1-1h3.5c.6 0 1 .4 1 1 0 1.3.2 2.5.6 3.6.1.3 0 .7-.2 1z"/></svg>
    888-555-0142
  </div>
  <nav class="nav">
    <span class="active">DONATE A CAR OR BOAT NOW</span><span>ABOUT</span><span>CONTACT</span><span>FAQ</span>
    <span class="search"><svg width="16" height="16" viewBox="0 0 16 16"><circle cx="6.5" cy="6.5" r="5" fill="none" stroke="#444" stroke-width="2"/><path d="M10 10l5 5" stroke="#444" stroke-width="2"/></svg></span>
  </nav>
</header>

<section class="hero" role="img" aria-label="Photo of three smiling women wearing pink ribbons outdoors">
  <h1 class="hero-title">Ready to Help Save Lives ? It's<br>Fast &amp; Easy !</h1>
  <p class="hero-sub">Your Vehicle Donation Helps Save Lives.</p>
  <span class="btn">DONATE NOW</span>
</section>

<section class="donate-band">
  <div class="ribbon-tab">
    <svg width="100" height="110" viewBox="0 0 100 110"><path d="M50 18c-10 0-14 10-10 20l-18 40 10 6 16-34 16 34 10-6-18-40c4-10 0-20-10-20z" fill="#f7d3e5"/></svg>
  </div>
  <h2 class="donate-title">DONATE YOUR CAR &amp; BOAT ONLINE</h2>
  <p class="donate-note">Full Tax Deduction - Running or Not</p>
  <div class="form-grid">
    <div class="field">Name *</div><div class="field">Phone *</div><div class="field select">Choose year *</div><div class="field">Vehical Model *</div>
    <div class="field">Email *</div><div class="field">Zipcode *</div><div class="field select">Choose Make*</div><div class="field submit">DONATE NOW</div>
  </div>
</section>

<section class="steps">
  <h2 class="section-title">3 SIMPLE STEP TO DONATE YOUR<br>CAR &amp; BOAT</h2>
  <div class="step-list">
    <div class="step">
      <div class="step-circle"><svg width="70" height="50" viewBox="0 0 70 50"><path d="M6 34V24l8-12h30l12 12h8v10z" fill="none" stroke="#e6197a" stroke-width="3"/><circle cx="18" cy="36" r="6" fill="#fff" stroke="#e6197a" stroke-width="3"/><circle cx="50" cy="36" r="6" fill="#fff" stroke="#e6197a" stroke-width="3"/></svg></div>
      <p>Fast Free Pickup -<br>24hr Response</p>
    </div>
    <div class="step">
      <div class="step-circle"><svg width="60" height="70" viewBox="0 0 60 70"><rect x="8" y="6" width="32" height="50" fill="none" stroke="#e6197a" stroke-width="3"/><path d="M15 18h18M15 26h18M15 34h10" stroke="#e6197a" stroke-width="3"/><ellipse cx="46" cy="52" rx="10" ry="4" fill="none" stroke="#e6197a" stroke-width="3"/><ellipse cx="46" cy="60" rx="10" ry="4" fill="none" stroke="#e6197a" stroke-width="3"/></svg></div>
      <p>Tax Deduction -<br>Easy To Do!</p>
    </div>
    <div class="step">
      <div class="step-circle"><svg width="50" height="66" viewBox="0 0 50 66"><rect x="5" y="8" width="40" height="54" fill="none" stroke="#e6197a" stroke-width="3"/><rect x="16" y="3" width="18" height="10" fill="#f1f1f1" stroke="#e6197a" stroke-width="3"/><path d="M13 26h24M13 36h24M13 46h16" stroke="#e6197a" stroke-width="3"/></svg></div>
      <p>Running or not - No<br>Emission Test Required</p>
    </div>
  </div>
</section>

<section class="why">
  <div class="why-photo" role="img" aria-label="Photo of young volunteers sitting around a donations poster"></div>
  <span class="round-arrow"><svg width="16" height="16" viewBox="0 0 16 16"><path d="M10 3L5 8l5 5" fill="none" stroke="#fff" stroke-width="2.5"/></svg></span>
  <div class="why-copy">
    <h2>WHY DONATE YOUR<br>CAR &amp; BOATE</h2>
    <p>Your car or boat donation helps support those stricken by breast cancer &amp; their families, and supports programs for screening, prevention, treatment and patient well being. Our operators are standing by 24 hours a day, 7 days a week to answer your questions and get your car or boat donation picked up quickly!</p>
    <span class="btn">LEARN MORE</span>
  </div>
</section>

<section class="veterans">
  <h2 class="section-title">DONATE YOU CAR TO VETERANS<br>MAKE A DIFFRENCE</h2>
  <div class="perk-list">
    <div class="perk"><div class="perk-circle"><svg width="44" height="44" viewBox="0 0 44 44"><rect x="8" y="4" width="26" height="34" fill="none" stroke="#fff" stroke-width="2.5"/><circle cx="30" cy="32" r="8" fill="#e6197a" stroke="#fff" stroke-width="2.5"/><path d="M25 37l10-10" stroke="#fff" stroke-width="2.5"/></svg></div><p>You have<br>no costs</p></div>
    <div class="perk"><div class="perk-circle"><svg width="54" height="40" viewBox="0 0 54 40"><path d="M4 28V16h18l6-8h10v20z" fill="none" stroke="#fff" stroke-width="2.5"/><path d="M38 12l12-8M50 4v14" stroke="#fff" stroke-width="2.5"/><circle cx="14" cy="30" r="5" fill="#e6197a" stroke="#fff" stroke-width="2.5"/><circle cx="34" cy="30" r="5" fill="#e6197a" stroke="#fff" stroke-width="2.5"/></svg></div><p>Free towing,<br>running or not</p></div>
    <div class="perk"><div class="perk-circle"><svg width="38" height="48" viewBox="0 0 38 48"><rect x="4" y="3" width="30" height="42" rx="3" fill="none" stroke="#fff" stroke-width="2.5"/><rect x="9" y="8" width="20" height="9" fill="none" stroke="#fff" stroke-width="2"/><path d="M10 24h4M18 24h4M26 24h2M10 31h4M18 31h4M26 31h2M10 38h4M18 38h4M26 38h2" stroke="#fff" stroke-width="2.5"/></svg></div><p>We issue you an<br>IRS tax receipt</p></div>
    <div class="perk"><div class="perk-circle"><svg width="38" height="48" viewBox="0 0 38 48"><path d="M4 3h20l10 10v32H4z" fill="none" stroke="#fff" stroke-width="2.5"/><path d="M24 3v10h10M10 24h18M10 31h18M10 38h12" stroke="#fff" stroke-width="2.5"/></svg></div><p>We take care of<br>all paperwork</p></div>
    <div class="perk"><div class="perk-circle"><svg width="50" height="40" viewBox="0 0 50 40"><path d="M6 24l6-12h26l6 12v8H6z" fill="none" stroke="#fff" stroke-width="2.5"/><path d="M14 12l-2-8M36 12l2-8" stroke="#fff" stroke-width="2.5"/><circle cx="15" cy="26" r="3" fill="#fff"/><circle cx="35" cy="26" r="3" fill="#fff"/></svg></div><p>No DMV<br>Hassles</p></div>
    <div class="perk"><div class="perk-circle"><svg width="48" height="44" viewBox="0 0 48 44"><rect x="4" y="14" width="40" height="26" fill="none" stroke="#fff" stroke-width="2.5"/><rect x="2" y="8" width="44" height="8" fill="none" stroke="#fff" stroke-width="2.5"/><path d="M24 8v32M24 8c-6-8-14-4-10 0M24 8c6-8 14-4 10 0" fill="none" stroke="#fff" stroke-width="2.5"/></svg></div><p>Vacation<br>Voucher</p></div>
  </div>
</section>

<section class="screening">
  <div class="screen-photo" role="img" aria-label="Photo of five women in pink shirts standing together"></div>
  <h3>Free Screening For Breast<br>Cancer</h3>
  <div class="checks">
    <span><svg width="20" height="20" viewBox="0 0 20 20"><circle cx="10" cy="10" r="9" fill="none" stroke="#fff" stroke-width="2"/><path d="M5.5 10l3 3 6-6" fill="none" stroke="#fff" stroke-width="2"/></svg>For YOU !</span>
    <span><svg width="20" height="20" viewBox="0 0 20 20"><circle cx="10" cy="10" r="9" fill="none" stroke="#fff" stroke-width="2"/><path d="M5.5 10l3 3 6-6" fill="none" stroke="#fff" stroke-width="2"/></svg>For a friend.</span>
    <span><svg width="20" height="20" viewBox="0 0 20 20"><circle cx="10" cy="10" r="9" fill="none" stroke="#fff" stroke-width="2"/><path d="M5.5 10l3 3 6-6" fill="none" stroke="#fff" stroke-width="2"/></svg>For someone in Your Family.</span>
  </div>
  <span class="btn btn-outline">DONATE NOW</span>
</section>

<section class="about">
  <div class="about-copy">
    <h2>ABOUT BREAST CANCER</h2>
    <h4>WHAT IS CANCER</h4>
    <p>Cancer is a group of many related diseases that begin in cells, the body's basic building blocks. To understand cancer, it is helpful to know what happens when normal cells become cancerous.</p>
    <span class="btn">LEARN MORE</span>
    <span class="org-link">Pink Horizon Cancer Alliance</span>
  </div>
  <div class="about-photo" role="img" aria-label="Photo of a crowd of women in pink raising joined hands at a charity walk"></div>
  <span class="round-arrow"><svg width="16" height="16" viewBox="0 0 16 16"><path d="M6 3l5 5-5 5" fill="none" stroke="#fff" stroke-width="2.5"/></svg></span>
</section>

<section class="faq">
  <h2 class="section-title">FAQ</h2>
  <div class="faq-list">
    <div class="faq-item open">Why donate a vehicle or vessel?<span class="toggle">+</span></div>
    <div class="faq-answer">To start, all you need to do is fill out an online application or give us a call! We will forward your information to a local towing company and they will call you. <a>Read More</a></div>
    <div class="faq-item">How do I donate a vehicle or vessel?<span class="toggle">−</span></div>
    <div class="faq-item">How does my vehicle or vessel donation benefit the charity?<span class="toggle">−</span></div>
    <div class="faq-item">How does donating a car or boat benefit my taxes?<span class="toggle">−</span></div>
    <div class="faq-item">How long does it take to pickup my donation?<span class="toggle">−</span></div>
    <div class="faq-item">What happens to my car after it's picked up?<span class="toggle">−</span></div>
    <div class="faq-item">Do I have any liability after the vehicle/vessel is picked up?<span class="toggle">−</span></div>
  </div>
</section>

<section class="pickup">
  <div class="pickup-band"></div>
  <div class="car-photo" role="img" aria-label="Photo of a pink ribbon-wrapped donation car"></div>
  <p class="pickup-label">FIRST FREE PICK UP</p>
  <p class="pickup-phone">888-555-0142</p>
</section>

<footer class="site-footer">
  <div class="foot-org"><span class="foot-square"></span><span class="foot-name">Pink Horizon Cancer Alliance</span></div>
  <p class="foot-text">Pink Horizon Cancer Alliance is a 501(c)(3) non-profit organization in full accordance with all laws and regulations of the US Government and the IRS. Your donation is tax-deductible in accordance with Federal regulations.</p>
  <p class="foot-copy">©RIDESFORPINKRIBBONAID.ORG - 2018 All Right Reserved.</p>
</footer>

</body>
</html>
```